Soap/cosmetic labels

Need labels that incorporate my brand , to fit onto rectangular and round labels readable down to two inches. Key ideas are luxury, nourishing, handmade, palm oil/paraben free, cruelty free, savon artisanal. One line will be called The Tender Cake by The Dune Wanderer with key words: fragrance free, all natural colorants. The other line is luxury oils, fragrance, indulgent and just The Dune Wanderer

Target Market(s)

Women mostly

Industry/Entity Type

cosmetics/soap

Colors
0094D4
00A9DD
6FCCEA
C7EBF8
E9F6FB

Requirements
Must have
• place for me to change fragrance and cosmetic type; gold goes on black labels; blue on white labels
Nice to have
• fit the brand

```html
<!DOCTYPE html>
<html lang="en">
<head>
<meta charset="utf-8">
<title>The Dune Wanderer – Round Soap Label (White)</title>
<link rel="stylesheet" href="https://fonts.googleapis.com/css2?family=Cinzel:wght@400;600;700&family=Italianno&display=swap">
<style>
  :root {
    --paper: #ffffff;
    --rim: #111111;
    --blue-deep: #0094D4;
    --blue-mid: #00A9DD;
    --blue-light: #6FCCEA;
    --blue-pale: #C7EBF8;
  }
  html, body {
    margin: 0;
    padding: 0;
    width: 1200px;
    height: 1200px;
    overflow: hidden;
    background: var(--paper);
  }
  .label-canvas {
    position: relative;
    width: 1200px;
    height: 1200px;
  }
  .label-art {
    position: absolute;
    inset: 0;
    width: 1200px;
    height: 1200px;
  }
  .outer-rim { fill: var(--paper); stroke: var(--rim); stroke-width: 5; }
  .inner-ring { fill: none; stroke: url(#blueSweep); stroke-width: 6; }
  .claims-ring {
    font-family: "Cinzel", serif;
    font-size: 36px;
    font-weight: 400;
    fill: var(--blue-mid);
    letter-spacing: 3px;
  }
  .brand-mark { fill: url(#blueSweep); }
  .brand-name {
    font-family: "Cinzel", serif;
    font-weight: 600;
    font-size: 80px;
    fill: var(--blue-deep);
  }
  .product-line {
    font-family: "Italianno", cursive;
    font-size: 84px;
    fill: var(--blue-mid);
  }
  .product-type {
    font-family: "Cinzel", serif;
    font-weight: 700;
    font-size: 42px;
    letter-spacing: 8px;
    fill: var(--blue-mid);
  }
</style>
</head>
<body>
<main class="label-canvas">
  <svg class="label-art" viewBox="0 0 1200 1200" xmlns="http://www.w3.org/2000/svg" aria-label="Round white soap label for The Dune Wanderer, luxury oils, fragrance">
    <defs>
      <linearGradient id="blueSweep" x1="0" y1="0" x2="1" y2="1">
        <stop offset="0" stop-color="#6FCCEA"/>
        <stop offset="0.55" stop-color="#0094D4"/>
        <stop offset="1" stop-color="#00A9DD"/>
      </linearGradient>
      <path id="claimsTop" d="M 205 441 A 420 420 0 0 1 1006 476"/>
      <path id="claimsBottom" d="M 1006 694 A 420 420 0 0 1 205 729"/>
    </defs>

    <circle class="outer-rim" cx="600" cy="585" r="505"/>
    <circle class="inner-ring" cx="600" cy="585" r="488"/>

    <text class="claims-ring">
      <textPath href="#claimsTop" startOffset="50%" text-anchor="middle" textLength="990" lengthAdjust="spacingAndGlyphs">SAVON ARTISANAL • HANDMADE</textPath>
    </text>
    <text class="claims-ring">
      <textPath href="#claimsBottom" startOffset="50%" text-anchor="middle" textLength="1030" lengthAdjust="spacingAndGlyphs">PALM OIL &amp; PARABEN FREE • CRUELTY FREE</textPath>
    </text>

    <circle class="brand-mark" cx="608" cy="360" r="88"/>

    <text class="brand-name" x="600" y="632" text-anchor="middle" textLength="820" lengthAdjust="spacingAndGlyphs">The Dune Wanderer</text>

    <text class="product-line" x="600" y="745" text-anchor="middle">luxury oils</text>
    <text class="product-type" x="600" y="850" text-anchor="middle">FRAGRANCE</text>
  </svg>
</main>
</body>
</html>
```